Make a medical leaflet for my patients undergoing ankle blocks

I have a very boring text only leaflet I would like to turn into a professional appealing medical leaflet to give to my patients. I would like to get this onto two pages of a4 if possible and its intended for electronic distribution mainly.
This will be for patients so it must be professional.
It must also contain a copyright logo on it and my name near the start (Dr Tobias Wendell) so my colleagues can't use it easily.
Target Market(s)
Patients undergoing surgery
Industry/Entity Type
Medical
Font styles to use
Other font styles liked:
- no idea, you tell me
Requirements
Must have
- the information contained on the attachment
- look professional
- a copyright on it
Nice to have
- the ashbury clinic logo
Should not have
- Any spelling, grammatical or linguistic errors
- Any font less than size 12

```html
<!DOCTYPE html>
<html lang="en">
<head>
<meta charset="utf-8">
<title>Ankle block – patient leaflet</title>
<link rel="stylesheet" href="https://fonts.googleapis.com/css2?family=Raleway:wght@300;400;500;700&display=swap">
<style>
  :root{
    --navy:#24487f;
    --brand:#1f5c9f;
    --tan:#d3c09b;
    --text:#5a5f68;
    --paper:#ffffff;
    --backdrop:#ececec;
    --sky:#dcebf8;
    --sand-1:#d9c29a;
    --sand-2:#efe3cc;
  }
  *{box-sizing:border-box;margin:0;padding:0}
  html,body{width:1200px;height:905px;overflow:hidden}
  body{background:var(--backdrop);font-family:"Raleway",Arial,sans-serif;color:var(--text);position:relative}

  .page{position:absolute;top:58px;width:547px;height:774px;background:var(--paper)}
  .page--front{left:43px}
  .page--back{left:621px}

  .sheet{position:absolute;left:23px;top:0;width:500px;height:774px;overflow:hidden}
  .page--front .sheet{background:linear-gradient(180deg,#fff 52%,#eaf2fb 72%,#c9def3 100%)}
  .page--back .sheet{left:29px;width:495px;background:linear-gradient(180deg,#3d7fc2 0%,#8cb9e3 22%,#d7e8f7 42%,#fff 62%)}

  .hero-photo{position:absolute;left:0;top:0;width:500px;height:290px;
    background:linear-gradient(160deg,var(--sand-2) 0%,#e6d3b0 40%,var(--sand-1) 100%)}
  .feet-photo{position:absolute;left:0;top:0;width:495px;height:140px;
    background:linear-gradient(180deg,#3b7dc0 0%,#5d97d0 60%,rgba(120,170,220,0) 100%)}

  .brand{position:absolute;display:flex;align-items:center;gap:12px;color:var(--navy);font-weight:400}
  .brand__mark{width:58px;height:58px;background:var(--brand);flex:none}
  .brand__text{line-height:1.1}
  .brand__name{font-size:22px;display:block}
  .brand__group{font-size:12px;display:block;margin-top:6px;padding-left:26px}
  .page--front .brand{left:30px;top:23px}

  .title{position:absolute;left:29px;top:102px;font-size:60px;font-weight:300;color:var(--navy);letter-spacing:.5px}
  .intro{position:absolute;left:29px;top:165px;width:345px;font-size:15.5px;line-height:18.5px;color:var(--navy);font-weight:400}
  .intro b{font-weight:700}

  .highlight{position:absolute;left:0;top:266px;width:500px;height:140px;background:var(--brand);
    border-top-right-radius:36px;display:flex;gap:30px;padding:18px 14px 0 27px;color:#fff;font-weight:700;font-size:10.6px;line-height:15.6px}
  .highlight__col{width:214px}
  .highlight__col:last-child{width:230px}
  .highlight__col p+p{margin-top:4px}

  .col{position:absolute;font-size:10.3px;line-height:12px}
  .col p{margin-bottom:7px}
  .tag{display:inline-block;background:var(--tan);color:#fff;font-size:12.5px;font-weight:400;padding:3px 24px 3px 16px;margin-bottom:10px;margin-left:-16px;border-top-right-radius:6px}
  .list{list-style:none}
  .list li{position:relative;padding-left:16px;margin-bottom:6px}
  .list li .n{position:absolute;left:0;top:0;color:var(--brand);font-weight:700}
  .sub{padding-left:16px}
  .bullets{list-style:none;padding-left:30px}
  .bullets li{margin-bottom:7px;text-indent:-6px}
  .bullets li::before{content:"• "}
  .indent{padding-left:16px}

  .front-left{left:23px;top:425px;width:230px}
  .front-left .tag{margin-left:-23px;padding-left:23px}
  .front-right{left:266px;top:430px;width:225px}

  .back-left{left:13px;top:143px;width:230px}
  .back-left .tag,.back-right .tag{margin-left:-13px;padding-left:13px}
  .back-right{left:252px;top:143px;width:236px}

  .copyright{position:absolute;font-size:8px;color:#6e90b8}
  .page--front .copyright{left:430px;top:739px}
  .page--back .copyright{left:443px;top:733px}

  .page--back .brand{left:40px;top:610px;flex-direction:column;align-items:flex-start;gap:14px}
  .page--back .brand__mark{width:68px;height:68px}

  .author{position:absolute;right:33px;top:697px;text-align:right;line-height:13px}
  .author__name{color:var(--navy);font-weight:700;font-size:12.5px}
  .author__mail{color:#4f86c0;font-size:12.5px}
</style>
</head>
<body>

<section class="page page--front">
  <div class="sheet">
    <div class="hero-photo" role="img" aria-label="Photograph of a person walking barefoot along a sandy beach"></div>

    <div class="brand">
      <span class="brand__mark"></span>
      <span class="brand__text">
        <span class="brand__name">Riverside Gate Hospital</span>
        <span class="brand__group">part of Meridian Health UK</span>
      </span>
    </div>

    <h1 class="title">Ankle block</h1>
    <p class="intro">You are scheduled to have surgery on your foot. It is my normal practice to offer and perform (with your consent) an <b>ankle block.</b> This is an optional injection of numbing liquid to the nerves which supply your foot.</p>

    <div class="highlight">
      <div class="highlight__col">
        <p>The ankle block can be performed when you are awake, sedated or under general anaesthesia. The ankle block can be combined with a general anaesthetic and with sedation. It can also be used to allow surgery to be performed with you wide awake in certain cases.</p>
      </div>
      <div class="highlight__col">
        <p>Having or not having an ankle block does not change the pre-operative fasting guidelines you have been given.</p>
        <p>There is a fee for performing an ankle block.</p>
        <p>Please consult my initial introductory email and terms of business for details</p>
      </div>
    </div>

    <div class="col front-left">
      <span class="tag">What are the benefits?</span>
      <ol class="list">
        <li><span class="n">1</span>Excellent pain relief - usually 10 - 14 hours (and rarely 24 - 48 hours)</li>
        <li><span class="n">2</span>Avoiding traditional painkillers, resulting in less post operative nausea and vomiting</li>
        <li><span class="n">3</span>The option to avoid a general anaesthetic (if you wish)</li>
        <li><span class="n">4</span>A faster recovery from the general anaesthetic</li>
        <li><span class="n">5</span>Certain surgery requires an overnight stay in hospital without an ankle block</li>
      </ol>
      <span class="tag">What are the risks?</span>
      <p>As with all injections, there is the risk of bruising, bleeding and infection.</p>
      <ol class="list">
        <li><span class="n">1</span>Nerve Damage - Occurs 1 in 5000 nerve blocks.</li>
      </ol>
      <p class="sub">Creates an area of numbness or weakness/ paralysis in some/all of the foot.</p>
      <p class="sub">Majority of nerve injuries will heal themselves within a year. There is no treatment to fix it.</p>
    </div>

    <div class="col front-right">
      <p class="indent">If the block has not worn off after 72 hours please let me know.</p>
      <ol class="list">
        <li><span class="n">2</span>Failure – The success rate with ankle blocks is 98 - 99%. Some blocks will fail, partially or totally.</li>
      </ol>
      <p class="indent">If total failure, I will discuss repeating the block with your consent.</p>
      <ol class="list">
        <li><span class="n">3</span>Pain during operation - If you choose to have wide awake surgery or surgery under sedation</li>
      </ol>
      <p class="indent">The surgery will stop and I will discuss three options with you</p>
      <ul class="bullets">
        <li>more numbing liquid to be injected by the surgeon</li>
        <li>more sedation / painkiller</li>
        <li>having a general anaesthetic</li>
      </ul>
      <p>If you decide to undergo surgery awake or sedated, there is a risk you will need to have a general anaesthetic if you feel pain. This is why the starvation instructions of awake surgery and general anaesthesia are the same.</p>
    </div>

    <p class="copyright">© Dr Tobias Wendell</p>
  </div>
</section>

<section class="page page--back">
  <div class="sheet">
    <div class="feet-photo" role="img" aria-label="Photograph of bare feet and ankles against a blue background"></div>

    <div class="col back-left">
      <span class="tag">How is it done?</span>
      <p>If you choose awake surgery or surgery with sedation -</p>
      <p>Numbing liquid is injected around the nerves which supply your foot.</p>
      <p>The ankle block takes 5 - 10 minutes to perform and requires 4 - 5 injections.</p>
      <p>Approximately 10 - 20 minutes to make your foot numb to pain.</p>
      <p>I will check the ankle block is working before we start surgery using cold spray.</p>
      <p>Sensations of touch, pressure, vibration and movement will still be felt.</p>
      <p>I will use a screen so you can't see the surgery (unless you would like to see).</p>
      <p>Some patients bring headphones to block out the noise of the operation.</p>
      <span class="tag">If you choose<br>a General anaesthetic</span>
      <p>I will perform the ankle block after I start the general anaesthetic.</p>
      <p>You should wake up from your surgery with a comfortable and numb foot/feet.</p>
      <p>If you wake in pain, we can repeat the ankle block or provide traditional painkillers.</p>
      <p>Whatever you choose, there will be a cannula placed in your hand and heart and oxygen monitoring throughout.</p>
    </div>

    <div class="col back-right">
      <span class="tag">After surgery</span>
      <p>You will go to the recovery area and then onto the ward when you are ready. It will be difficult to walk while the block is working so physiotherapists will help you first walk. If you need crutches they will teach you how to use them.</p>
      <p>Your foot will be numb and so you will not feel where your foot is in relation to nearby objects. As a result, it is easy to knock your foot. Please take extra care while your foot is still numb.</p>
      <p>As the block wears off, the foot may feel slightly painful, tingly or hot. At this point you should take your painkillers I have prescribed. Depending on your medical history you will have up to three painkillers. I would suggest to start with all three. You will also have an anti-sickness prescribed if one of the painkillers (typically codeine or morphine) makes you feel sick.</p>
      <p>Occasionally (1 - 2%), pain when the block wears off will be severe. In this case contact your surgeon's secretary. We can use stronger pain medication, but there will be a charge in writing and getting the private prescription to you (please see my terms of business) via courier.</p>
      <span class="tag">The alternative</span>
      <p>If you do not have an ankle block your surgery can still proceed.</p>
      <p>Post operative pain can be managed with traditional painkillers.</p>
      <p>However, you are more likely to need an overnight stay or feel sick after the anaesthetic.</p>
      <p>If you have any further questions about an ankle block I will see you the day of your surgery.</p>
      <p>Alternatively, you can request the following optional services (as mentioned in my terms of business).</p>
    </div>

    <div class="brand">
      <span class="brand__mark"></span>
      <span class="brand__text">
        <span class="brand__name">Riverside Gate Hospital</span>
        <span class="brand__group">part of Meridian Health UK</span>
      </span>
    </div>

    <div class="author">
      <div class="author__name">Dr Tobias Wendell</div>
      <div class="author__mail">email: address to be inserted here</div>
    </div>

    <p class="copyright">© Dr Tobias Wendell</p>
  </div>
</section>

</body>
</html>
```